Tallbridge needs a new rocket based website

We need a new website that will be based on our rocket ship logo. We develop innovative solutions for enterprises. We would like to see a design that when the pages scroll, the rocket launches and goes from launch through a journey, similar to how we approach our customer. We would like areas for "Who are we", "What can we do", "What have we done", "How can we help". http://www.tallbridge.com.au is our current website

Target Market(s)

Government, Enterprise, Cloud

Industry/Entity Type

Software Service

Coding

Coded - Design and coding required

Number of Pages Required

2 page

Requirements
Must have
• We would like to see a design that when the pages scroll, the rocket launches and goes from launch through a journey, similar to how we approach our customer.
• Must have a home page and a detail page.
• Would like to see the logo/rocket animate in some way when you scroll through he page.

```html
<!DOCTYPE html>
<html lang="en">
<head>
<meta charset="utf-8">
<title>Tallbridge – Innovative Software Solutions</title>
<link href="https://fonts.googleapis.com/css2?family=Mulish:wght@400;600;700;800&display=swap" rel="stylesheet">
<style>
:root{
  --orange:#f7931e;
  --orange-deep:#ec5a1c;
  --red:#c8102e;
  --ink:#1c1c1c;
  --text:#555;
  --grey-band:#f4f5f7;
  --teal:#12c39a;
  --cloud:#f7931e;
  --blue:#1fa9dd;
  --green:#8cc63f;
  --dark:#1b1b1d;
  --white:#fff;
  --nav-active:#ffcf5c;
}
*{box-sizing:border-box;margin:0;padding:0}
html,body{width:1200px;height:4390px;overflow:hidden}
body{font-family:"Mulish",Arial,sans-serif;color:var(--text);background:var(--white);position:relative}
.abs{position:absolute}
.btn{position:absolute;height:40px;border-radius:20px;background:linear-gradient(90deg,var(--orange),var(--orange-deep));color:var(--white);font-size:13px;font-weight:700;display:flex;align-items:center;justify-content:center;box-shadow:0 6px 14px rgba(236,90,28,.3)}
h2{position:absolute;font-size:40px;font-weight:800;color:var(--ink);white-space:nowrap}
p{font-size:13px;line-height:1.6}
.img-fill{position:absolute}

/* header */
.brand{left:92px;top:26px;display:flex;align-items:center;gap:8px;font-size:24px;font-weight:800;color:var(--ink)}
.brand-dot{width:10px;height:10px;background:var(--orange);border-radius:50%}
.nav{left:602px;top:34px;display:flex;gap:52px;font-size:14px;color:var(--white)}
.nav .active{color:var(--nav-active);font-weight:700}
.phone{left:990px;top:32px;display:flex;align-items:center;gap:10px;font-size:16px;font-weight:700;color:var(--white)}

/* hero */
.hero-title{left:92px;top:212px;font-size:66px;font-weight:800;color:var(--ink)}
.hero-sub{left:92px;top:292px;font-size:30px;font-weight:400;color:#333;letter-spacing:1px}

/* services */
.services-band{left:0;top:987px;width:1200px;height:713px;background:var(--grey-band)}
.pill{position:absolute;height:46px;border-radius:23px;display:flex;align-items:center;color:var(--white);font-size:12px;white-space:nowrap}
.pill strong{font-size:14px;margin-right:20px}
.pill-icon{position:absolute;width:70px;height:70px;border-radius:50%;background:var(--white);display:flex;align-items:center;justify-content:center;box-shadow:0 4px 10px rgba(0,0,0,.12)}
.pill-icon span{width:54px;height:54px;border-radius:50%;display:flex;align-items:center;justify-content:center}

/* done */
.card-title{position:absolute;font-size:17px;font-weight:800;color:var(--ink)}
.card-text{position:absolute;width:316px;font-size:12px}

/* can do */
.cando-band{left:0;top:2410px;width:1200px;height:585px;background:var(--grey-band)}
.cell{position:absolute;width:198px;text-align:center;font-size:13px;font-weight:700;color:var(--ink)}
.cell svg{display:block;margin:0 auto 18px}

/* contact */
.info-box{left:755px;top:3622px;width:351px;height:200px;background:#2a2a2c;color:#ddd;padding:26px 28px;font-size:12px;line-height:1.7}
.info-box .brand-sm{font-size:22px;font-weight:800;color:var(--orange);margin-bottom:12px}
.info-row{display:flex;gap:10px;align-items:flex-start;margin-bottom:6px}
.footer{left:0;top:3940px;width:1200px;height:450px;background:var(--dark)}
.field{position:absolute;height:30px;border-bottom:1px solid #555;font-size:12px;color:#ccc}
</style>
</head>
<body>

<!-- hero -->
<svg class="abs" style="left:0;top:0" width="1200" height="580" aria-hidden="true">
  <defs>
    <linearGradient id="heroWave" x1="0" y1="0" x2="1" y2="1">
      <stop offset="0" stop-color="#a8102a"/>
      <stop offset=".5" stop-color="#e8401c"/>
      <stop offset="1" stop-color="#f7931e"/>
    </linearGradient>
  </defs>
  <circle cx="40" cy="110" r="130" fill="none" stroke="#f1f1f1" stroke-width="2"/>
  <circle cx="40" cy="110" r="200" fill="none" stroke="#f4f4f4" stroke-width="2"/>
  <path d="M470 0 H1200 V577 H430 C600 560 760 520 785 440 C805 365 690 305 645 225 C600 145 560 105 525 65 C500 40 482 20 470 0 Z" fill="url(#heroWave)"/>
  <g stroke="#ffb25a" stroke-width="6" stroke-linecap="round" opacity=".7">
    <line x1="1075" y1="390" x2="1135" y2="455"/>
    <line x1="1110" y1="372" x2="1175" y2="442"/>
    <line x1="1045" y1="430" x2="1090" y2="480"/>
  </g>
</svg>
<div class="img-fill" role="img" aria-label="Illustration of a white rocket with a blue porthole launching upward on orange flames" style="left:805px;top:110px;width:190px;height:390px;border-radius:95px 95px 40px 40px;background:linear-gradient(180deg,#ffffff 0%,#eef0f4 45%,#ffd27a 75%,#f7931e 100%);box-shadow:0 10px 30px rgba(120,20,10,.25);transform:rotate(-14deg)"></div>

<div class="abs brand"><span class="brand-dot"></span>Tallbridge</div>
<nav class="abs nav"><span class="active">Home</span><span>About</span><span>Services</span><span>Contact</span></nav>
<div class="abs phone">
  <svg width="16" height="16" viewBox="0 0 24 24"><path fill="#fff" d="M6.6 10.8a15 15 0 006.6 6.6l2.2-2.2a1 1 0 011-.25 11.4 11.4 0 003.6.6 1 1 0 011 1V20a1 1 0 01-1 1A17 17 0 013 4a1 1 0 011-1h3.5a1 1 0 011 1 11.4 11.4 0 00.6 3.6 1 1 0 01-.25 1z"/></svg>
  1300 482 117
</div>
<h1 class="abs hero-title">Tallbridge</h1>
<div class="abs hero-sub">Innovative Software Solutions</div>
<div class="btn" style="left:92px;top:352px;width:172px">Find Out More</div>

<!-- who are we -->
<div class="img-fill" role="img" aria-label="Illustration of a person presenting charts on a large dashboard screen" style="left:130px;top:630px;width:410px;height:310px;border-radius:50%;background:radial-gradient(ellipse at center,#e3ecfb 0%,#eef3fc 60%,#fff 100%)"></div>
<h2 style="left:668px;top:680px">Who Are We</h2>
<p class="abs" style="left:668px;top:748px;width:440px;font-size:12px">Offering the latest in enterprise architecture, design and development of bespoke software solutions. Always researching and implementing the latest technology for customers.</p>
<div class="btn" style="left:668px;top:836px;width:126px">Read More</div>

<!-- services -->
<div class="abs services-band"></div>
<h2 style="left:0;width:1200px;text-align:center;top:1096px">Our Services</h2>
<div class="img-fill" role="img" aria-label="Photo of a laptop and coffee on a desk" style="left:95px;top:1100px;width:450px;height:495px;border-radius:50%;background:linear-gradient(135deg,#d9d4cc,#f2efe9 50%,#9aa3ad);border:6px solid #e6e8ec"></div>

<div class="pill" style="left:540px;top:1220px;width:564px;background:var(--teal);padding-left:86px"><strong>e-Parliament</strong>All of your Parliamentary software and business process needs</div>
<div class="pill" style="left:540px;top:1325px;width:535px;background:var(--cloud);padding-left:86px"><strong>Cloud</strong>Cloud Office Suites, Migration, Security, Customisations</div>
<div class="pill" style="left:540px;top:1433px;width:505px;background:var(--blue);padding-left:86px"><strong>Architecture and Design</strong>Business process design, technology</div>
<div class="pill" style="left:430px;top:1544px;width:586px;background:var(--green);padding-left:86px"><strong>Software Development</strong>Software development including business apps</div>

<div class="pill-icon" style="left:515px;top:1208px"><span style="background:var(--teal)"><svg width="26" height="26" viewBox="0 0 24 24" fill="none" stroke="#fff" stroke-width="1.6"><rect x="5" y="3" width="14" height="18"/><path d="M9 16l3-8 3 8M10 13h4"/></svg></span></div>
<div class="pill-icon" style="left:515px;top:1313px"><span style="background:var(--cloud)"><svg width="26" height="26" viewBox="0 0 24 24" fill="none" stroke="#fff" stroke-width="1.6"><path d="M7 18a4 4 0 010-8 5 5 0 019.6-1A3.5 3.5 0 0117 18z"/><path d="M12 11v6M9.5 14l2.5-3 2.5 3"/></svg></span></div>
<div class="pill-icon" style="left:515px;top:1421px"><span style="background:var(--blue)"><svg width="26" height="26" viewBox="0 0 24 24" fill="none" stroke="#fff" stroke-width="1.6"><path d="M4 20l6-6M10 4l10 10-4 4L6 8z"/></svg></span></div>
<div class="pill-icon" style="left:405px;top:1532px"><span style="background:var(--green)"><svg width="26" height="26" viewBox="0 0 24 24" fill="none" stroke="#fff" stroke-width="1.6"><rect x="4" y="5" width="16" height="12"/><path d="M9 9l-2 2 2 2M15 9l2 2-2 2M8 20h8"/></svg></span></div>

<!-- what have we done -->
<h2 style="left:0;width:1200px;text-align:center;top:1806px">What Have We Done</h2>
<p class="abs" style="left:235px;top:1876px;width:730px;text-align:center;font-size:12px">Lorem ipsum dolor sit amet, consectetur adipiscing elit. Duis nibh est, consectetur ac massa eget, condimentum consequat tellus. Phasellus ligula magna, ultrices sit amet mi quis.</p>

<div class="img-fill" role="img" aria-label="Photo of a man working on a laptop on a sofa" style="left:94px;top:1962px;width:316px;height:210px;background:linear-gradient(135deg,#6f8597,#c9d3db 60%,#3b4a57)"></div>
<div class="img-fill" role="img" aria-label="Photo of colleagues working together at laptops" style="left:442px;top:1962px;width:316px;height:210px;background:linear-gradient(135deg,#b7a48f,#e7e2da 55%,#6b6f74)"></div>
<div class="img-fill" role="img" aria-label="Photo of hands typing on a laptop on a white desk" style="left:790px;top:1962px;width:316px;height:210px;background:linear-gradient(135deg,#f1f1f1,#d8d8da 55%,#7a3b6a)"></div>

<div class="card-title" style="left:94px;top:2200px">Lorem ipsum dolor</div>
<div class="card-title" style="left:442px;top:2200px">Lorem ipsum dolor</div>
<div class="card-title" style="left:790px;top:2200px">Lorem ipsum dolor</div>
<p class="card-text" style="left:94px;top:2240px">Lorem ipsum dolor sit amet, consectetur adipiscing elit. Duis nibh est, consectetur ac massa eget, condimentum consequat tellus.</p>
<p class="card-text" style="left:442px;top:2240px">Lorem ipsum dolor sit amet, consectetur adipiscing elit. Duis nibh est, consectetur ac massa eget, condimentum consequat tellus.</p>
<p class="card-text" style="left:790px;top:2240px">Lorem ipsum dolor sit amet, consectetur adipiscing elit. Duis nibh est, consectetur ac massa eget, condimentum consequat tellus.</p>

<!-- what can we do -->
<div class="abs cando-band"></div>
<svg class="abs" style="left:95px;top:2515px" width="400" height="380" aria-hidden="true">
  <defs>
    <linearGradient id="blob" x1="0" y1="0" x2="1" y2="1">
      <stop offset="0" stop-color="#f7931e"/>
      <stop offset="1" stop-color="#d8301c"/>
    </linearGradient>
  </defs>
  <path d="M60 70 C130 10 300 -10 360 80 C410 160 360 300 250 350 C150 390 20 360 8 250 C0 170 10 110 60 70 Z" fill="url(#blob)"/>
</svg>
<h2 style="left:132px;top:2610px;color:var(--white);font-size:36px;line-height:1.15;width:300px">What Can<br>We Do</h2>
<p class="abs" style="left:132px;top:2702px;width:340px;color:#fff;font-size:12px;line-height:1.5">Lorem ipsum dolor sit amet, consectetur adipiscing elit. Duis nibh est, consectetur ac massa eget, condimentum consequat tellus. Phasellus ligula magna.</p>
<div class="abs" style="left:132px;top:2778px;width:126px;height:38px;border:1.5px solid #fff;border-radius:19px;color:#fff;font-size:13px;font-weight:700;display:flex;align-items:center;justify-content:center">Read More</div>

<svg class="abs" style="left:512px;top:2535px" width="594" height="330" aria-hidden="true">
  <g stroke="#f29a7a" stroke-width="1">
    <line x1="198" y1="0" x2="198" y2="330"/><line x1="396" y1="0" x2="396" y2="330"/>
    <line x1="0" y1="155" x2="594" y2="155"/>
  </g>
</svg>
<div class="cell" style="left:512px;top:2570px"><svg width="46" height="40" viewBox="0 0 46 40" fill="none" stroke="#ec5a1c" stroke-width="1.6"><rect x="6" y="6" width="34" height="22"/><path d="M2 32h42"/></svg>Lorem ipsum dolor</div>
<div class="cell" style="left:710px;top:2570px"><svg width="46" height="40" viewBox="0 0 46 40" fill="none" stroke="#ec5a1c" stroke-width="1.6"><rect x="6" y="4" width="34" height="30"/><circle cx="23" cy="20" r="7"/><path d="M6 10h34"/></svg>Lorem ipsum dolor</div>
<div class="cell" style="left:908px;top:2570px"><svg width="46" height="40" viewBox="0 0 46 40" fill="none" stroke="#ec5a1c" stroke-width="1.6"><rect x="6" y="10" width="28" height="24"/><circle cx="34" cy="10" r="6"/><path d="M12 28V20M18 28V16M24 28V22"/></svg>Lorem ipsum dolor</div>
<div class="cell" style="left:512px;top:2728px"><svg width="46" height="40" viewBox="0 0 46 40" fill="none" stroke="#ec5a1c" stroke-width="1.6"><path d="M13 26a7 7 0 010-14 9 9 0 0117-2 6 6 0 011 16z"/><path d="M16 30v6M23 30v6M30 30v6"/></svg>Lorem ipsum dolor</div>
<div class="cell" style="left:710px;top:2728px"><svg width="46" height="40" viewBox="0 0 46 40" fill="none" stroke="#ec5a1c" stroke-width="1.6"><rect x="10" y="4" width="22" height="32"/><circle cx="30" cy="24" r="7"/><path d="M15 12h12M15 18h8"/></svg>Lorem ipsum dolor</div>
<div class="cell" style="left:908px;top:2728px"><svg width="46" height="40" viewBox="0 0 46 40" fill="none" stroke="#ec5a1c" stroke-width="1.6"><rect x="6" y="6" width="34" height="26"/><path d="M6 12h34M14 20h18M14 26h12"/></svg>Lorem ipsum dolor</div>

<!-- how can we help -->
<div class="img-fill" role="img" aria-label="Close-up photo of hands typing on a laptop keyboard" style="left:94px;top:3110px;width:500px;height:280px;background:linear-gradient(120deg,#1f3242,#5f7d93 55%,#2a3b49)"></div>
<h2 style="left:662px;top:3100px">How Can We Help</h2>
<p class="abs" style="left:662px;top:3170px;width:444px;font-size:12px">Lorem ipsum dolor sit amet, consectetur adipiscing elit. Duis nibh est, consectetur ac massa eget, condimentum consequat tellus. Phasellus ligula magna, ultrices sit amet mi quis, efficitur accumsan eros. Morbi accumsan, nisi vitae lobortis semper, lacus justo condimentum arcu, ut finibus mauris tortor tincidunt ipsum.</p>
<div class="btn" style="left:662px;top:3298px;width:126px">Read More</div>

<!-- map -->
<div class="img-fill" role="img" aria-label="Street map showing the office location" style="left:0;top:3505px;width:1200px;height:435px;background:linear-gradient(135deg,#e5e3df,#eeede9 50%,#dcdad5)"></div>
<svg class="abs" style="left:636px;top:3700px" width="26" height="36" viewBox="0 0 24 34" aria-hidden="true"><path d="M12 0a11 11 0 0111 11c0 8-11 23-11 23S1 19 1 11A11 11 0 0112 0z" fill="#e53935"/><circle cx="12" cy="11" r="4" fill="#a01818"/></svg>
<div class="abs info-box">
  <div class="brand-sm">Tallbridge</div>
  <div class="info-row"><svg width="12" height="14" viewBox="0 0 24 30"><path d="M12 0a11 11 0 0111 11c0 8-11 19-11 19S1 19 1 11A11 11 0 0112 0z" fill="#f7931e"/></svg><span>Unit 7, 41 Kestrel St<br>Marden, SA 5070</span></div>
  <div class="info-row"><svg width="12" height="12" viewBox="0 0 24 24"><path fill="#f7931e" d="M6.6 10.8a15 15 0 006.6 6.6l2.2-2.2a1 1 0 011-.25 11.4 11.4 0 003.6.6 1 1 0 011 1V20a1 1 0 01-1 1A17 17 0 013 4a1 1 0 011-1h3.5a1 1 0 011 1 11.4 11.4 0 00.6 3.6 1 1 0 01-.25 1z"/></svg><span>1300 482 117</span></div>
  <div class="info-row"><svg width="12" height="12" viewBox="0 0 24 24" fill="none" stroke="#f7931e" stroke-width="2"><rect x="2" y="5" width="20" height="14"/><path d="M2 5l10 8 10-8"/></svg><span>info@tallbridge.com.au</span></div>
</div>

<!-- footer -->
<div class="abs footer"></div>
<h2 style="left:0;width:1200px;text-align:center;top:4040px;color:#fff;font-size:28px">Get In Touch</h2>
<div class="field" style="left:234px;top:4090px;width:366px">Name</div>
<div class="field" style="left:606px;top:4090px;width:360px">Email</div>
<div class="field" style="left:234px;top:4128px;width:366px">Phone</div>
<div class="field" style="left:606px;top:4128px;width:360px">Subject</div>
<div class="field" style="left:234px;top:4172px;width:732px">Message</div>
<div class="btn" style="left:556px;top:4226px;width:124px;height:36px">Send</div>
<div class="abs" style="left:92px;top:4340px;width:30px;height:30px;border-radius:50%;background:#fff"></div>
<div class="abs" style="left:800px;top:4348px;width:306px;text-align:right;font-size:11px;color:#999">© 2018 <span style="color:var(--orange)">Tallbridge</span>. All Right Reserved</div>

</body>
</html>
```